Modellprojekt in der Jugendhilfe sucht für Abschlussbroschüre ansprechendes Design
Zielgruppe
Wir sind ein Jugendhilfeträger und haben kürzlich ein dreijähriges Modellprojekt 'Qualitätsmarke-Gemeinsame Familienbegleitung' (Signet 'QM_Anerkennung' liegt anbei) beendet. Zielgruppen sind zum Einen Kinder und Jugendliche, die in Erziehungshilfe-Wohngruppen leben und zum Anderen Fach- und Führungskräfte in der Kinder- und Jugendhilfe. Über Ablauf und Schlussfolgerungen aus dem abgeschlossenen Modellprojekt soll eine 30-seitige Broschüre mit dem Titel 'Hier wächst Mitsprache' Untertitel 'Ein Wegweiser zur Qualitätsmarke' Auskunft geben.
Aufgabenstellung
- Broschüre im DIN A4 - Format,
- Dummy-Text für Projektstruktur und -beteiligte,
- Formschönes und dynamisches Design,
- Platzhalter für eigene Bilder (max. 3 pro Seite),
- die 6 Einrichtungslogos in einer Reihe auf dem Deckblatt vorne (unten),
- Der Broschüreninhalt ist in der PDF 'Kurzvorstellung enthalten',
- Vorgaben zum CD im PDF 'Hauptmanual KWF',
- Das KWF-Signet, wie im Manual beschrieben,
- das ebenfalls hochgeladene Qualitätsmarke kommt auf das Deckblatt

```html
<!DOCTYPE html>
<html lang="de">
<head>
<meta charset="utf-8">
<title>Hier wächst Mitsprache – Broschüre</title>
<link rel="stylesheet" href="https://fonts.googleapis.com/css2?family=Montserrat:wght@600;700;800&family=Open+Sans:wght@400;600;700&display=swap">
<style>
  :root{
    --blue:#0b5c96;
    --blue-light:#a9c0de;
    --ink:#333b44;
    --paper:#ffffff;
    --stage:#e4e5e7;
  }
  *{box-sizing:border-box;margin:0;padding:0}
  html,body{width:835px;height:1200px;overflow:hidden;background:var(--stage)}
  body{position:relative;font-family:"Open Sans",Arial,sans-serif;color:var(--ink)}
  .spread{position:absolute;left:20px;width:795px;height:562px;display:flex;box-shadow:0 6px 18px rgba(0,0,0,.18)}
  .spread--outer{top:28px}
  .spread--inner{top:612px}
  .page{position:relative;width:397.5px;height:562px;background:var(--paper);overflow:hidden}

  /* back cover */
  .back__band{position:absolute;left:0;top:0;width:100%;height:100px;background:var(--blue)}
  .back__photo{position:absolute;left:0;top:100px;width:100%;height:340px;
    background:linear-gradient(135deg,#c7a485 0%,#8d5f3f 45%,#4b3020 100%)}
  .back__strip{position:absolute;left:0;top:440px;width:100%;height:52px;background:var(--blue-light)}
  .back__network{position:absolute;left:48px;top:456px;font-size:17px;color:var(--blue);font-weight:600}
  .brandmark{position:absolute;display:flex;align-items:center;gap:6px}
  .brandmark__square{display:block;background:var(--blue)}
  .brandmark__name{font-family:"Montserrat",sans-serif;font-weight:800;color:var(--blue)}
  .back__brand{right:10px;top:428px;flex-direction:column;gap:2px}
  .back__brand .brandmark__square{width:42px;height:46px}
  .back__brand .brandmark__name{font-size:13px}
  .contact{position:absolute;left:14px;top:500px;list-style:none;font-size:9.5px;line-height:12px;color:var(--ink)}
  .contact li{display:flex;align-items:center;gap:8px}
  .contact svg{width:10px;height:10px;flex:none}

  /* front cover */
  .front__head{position:absolute;left:0;top:0;width:100%;height:100px;background:var(--paper)}
  .front__block{position:absolute;right:0;top:0;width:52%;height:100px;background:var(--blue)}
  .front__brand{left:16px;top:14px;gap:8px;align-items:flex-start}
  .front__brand .brandmark__square{width:40px;height:58px}
  .front__brand .brandmark__name{font-size:12px;line-height:1}
  .front__brand small{display:block;font-family:"Open Sans",sans-serif;font-weight:400;font-size:7.5px;line-height:9px;color:#222;margin-top:3px}
  .front__photo{position:absolute;left:0;top:100px;width:100%;height:300px;
    background:radial-gradient(circle at 50% 45%,#e8b79a 0%,#d9a07c 25%,#c44a4a 42%,#3f8a3a 70%,#2e6a2b 100%)}
  .front__titleband{position:absolute;left:0;top:400px;width:100%;height:56px;background:var(--blue-light);
    display:flex;flex-direction:column;justify-content:center;align-items:center}
  .front__title{font-family:"Montserrat",sans-serif;font-weight:800;font-size:15px;color:var(--blue);letter-spacing:.5px;line-height:19px}
  .front__subtitle{font-family:"Montserrat",sans-serif;font-weight:600;font-size:13px;color:var(--blue);letter-spacing:.4px;line-height:17px}
  .partners{position:absolute;left:10px;right:10px;top:476px;display:flex;align-items:center;justify-content:space-between}
  .partner{display:flex;align-items:center;gap:3px;font-size:6px;font-weight:600;color:#2a2f36;line-height:7px;max-width:56px}
  .partner i{display:block;width:8px;height:8px;background:var(--blue-light);flex:none}
  .seal{width:30px;height:30px;border-radius:50%;background:#2f7d3b;flex:none}

  /* contents page */
  .contents{background:var(--blue);color:#fff}
  .contents__title{position:absolute;left:58px;top:140px;font-family:"Montserrat",sans-serif;font-weight:800;font-size:23px;letter-spacing:1.5px}
  .toc{position:absolute;left:40px;top:196px;list-style:none;border-left:1px solid rgba(255,255,255,.85);margin-left:62px;padding-left:10px}
  .toc li{position:relative;height:26px;font-size:9px;line-height:11px;display:flex;align-items:center}
  .toc__num{position:absolute;right:calc(100% + 22px);font-family:"Montserrat",sans-serif;font-weight:700;font-size:14px;white-space:nowrap}
  .contents__photo{position:absolute;left:28px;bottom:0;width:340px;height:150px;border-radius:110px 110px 0 0;
    background:linear-gradient(90deg,#5b3a2c 0%,#e0b38f 30%,#a8408f 55%,#2f8f4a 80%,#b23a3a 100%)}

  /* foreword page */
  .portrait{position:absolute;left:44px;top:112px;width:100px;height:116px;background:linear-gradient(160deg,#f1f1f1 0%,#d8b39a 45%,#2d2f3a 100%)}
  .person__name{position:absolute;left:152px;top:94px;font-family:"Montserrat",sans-serif;font-weight:800;font-size:20px;color:var(--blue);white-space:nowrap}
  .person__role{position:absolute;left:154px;top:120px;font-size:11px;color:#444}
  .person__text{position:absolute;left:154px;top:142px;width:212px;font-size:6.9px;line-height:9.4px;text-align:justify;color:#2b2b2b}
  .person__text p+p{margin-top:0}
  .person__contact{position:absolute;left:154px;top:348px;font-size:7px;line-height:10px;color:#2b2b2b}
  .person__contact b{color:var(--blue)}
  .folio{position:absolute;right:22px;bottom:18px;font-size:7px;font-weight:700;color:var(--blue)}
</style>
</head>
<body>

<section class="spread spread--outer">
  <article class="page back">
    <div class="back__band"></div>
    <div class="back__photo" role="img" aria-label="Foto: viele aufeinandergelegte Hände als Zeichen des Zusammenhalts"></div>
    <div class="back__strip"></div>
    <p class="back__network">JugendhilfeVerbund Küstenland</p>
    <div class="brandmark back__brand"><span class="brandmark__square"></span><span class="brandmark__name">KWF</span></div>
    <ul class="contact">
      <li><svg viewBox="0 0 10 10"><circle cx="5" cy="5" r="5" fill="#0b5c96"/><path d="M5 2.2a1.8 1.8 0 0 1 1.8 1.8c0 1.3-1.8 3.6-1.8 3.6S3.2 5.3 3.2 4A1.8 1.8 0 0 1 5 2.2z" fill="#fff"/></svg>Lindenweg 8</li>
      <li><svg viewBox="0 0 10 10"></svg>24100 Hafenstadt</li>
      <li><svg viewBox="0 0 10 10"><circle cx="5" cy="5" r="5" fill="#0b5c96"/><path d="M3 2.6l1 .2.4 1.3-.6.5a4 4 0 0 0 1.6 1.6l.5-.6 1.3.4.2 1c-2.8.6-5-1.6-4.4-4.4z" fill="#fff"/></svg>0 40 12 | 5 67-0</li>
      <li><svg viewBox="0 0 10 10"><circle cx="5" cy="5" r="5" fill="#0b5c96"/><rect x="2.6" y="3.3" width="4.8" height="3.4" fill="#fff"/><path d="M2.6 3.3L5 5.2l2.4-1.9" stroke="#0b5c96" stroke-width=".6" fill="none"/></svg>info@jugendverbund-kl.de</li>
      <li><svg viewBox="0 0 10 10"><circle cx="5" cy="5" r="5" fill="#0b5c96"/><circle cx="5" cy="5" r="2.6" stroke="#fff" stroke-width=".6" fill="none"/><path d="M2.4 5h5.2M5 2.4v5.2" stroke="#fff" stroke-width=".5"/></svg>www.jugendverbund-kl.de</li>
    </ul>
  </article>

  <article class="page front">
    <div class="front__head"></div>
    <div class="front__block"></div>
    <div class="brandmark front__brand">
      <span class="brandmark__square"></span>
      <span class="brandmark__name">KWF<small>Gruppe<br>Küstenwerk<br>für Fürsorge</small></span>
    </div>
    <div class="front__photo" role="img" aria-label="Foto: lachende Kinder liegen im Kreis im Gras und formen mit den Händen Ferngläser"></div>
    <div class="front__titleband">
      <h1 class="front__title">HIER WÄCHST MITSPRACHE</h1>
      <p class="front__subtitle">EIN WEGWEISER ZUR QUALITÄTSMARKE</p>
    </div>
    <div class="partners">
      <span class="partner"><i></i>Kinderhaus Seeblick</span>
      <span class="partner"><i></i>Hilfen Moorland</span>
      <span class="partner"><i></i>Wegbegleiter Nord</span>
      <span class="partner"><i></i>Jugendhaus Auental</span>
      <span class="partner"><i></i>Arbeitskreis Förde</span>
      <span class="partner"><i></i>Jugendhilfe Dünenland</span>
      <span class="seal" role="img" aria-label="Qualitätsmarke-Siegel"></span>
    </div>
  </article>
</section>

<section class="spread spread--inner">
  <article class="page contents">
    <h2 class="contents__title">INHALTSVERZEICHNIS</h2>
    <ol class="toc">
      <li><span class="toc__num">01</span>Danksagung J. Brettschneider</li>
      <li><span class="toc__num">02-03</span>Erfolgsstory</li>
      <li><span class="toc__num">04</span>Hier wächst Mitsprache<br>eine partizipative Lernreise</li>
      <li><span class="toc__num">05-06</span>Lernreiseteilnehmer - QM-Projekt kurz und knapp mit Foto:</li>
      <li><span class="toc__num">07-11</span>Ladestationen auf dem Weg zur Qualitätsmarke</li>
      <li><span class="toc__num">12-15</span>Lernreise-Highlight Campus – Ein Erlebnis mit Ergebnis</li>
      <li><span class="toc__num">19-21</span>Heimkehr / Finale mit Befragung</li>
      <li><span class="toc__num">22-26</span>Zum Abschluss: Ihr Fahrplan zur „Qualitätsmarke“</li>
    </ol>
    <div class="contents__photo" role="img" aria-label="Foto: Gruppe lachender Kinder liegt nebeneinander"></div>
  </article>

  <article class="page foreword">
    <div class="portrait" role="img" aria-label="Porträtfoto der Einrichtungsleitung"></div>
    <h2 class="person__name">Jonas Brettschneider</h2>
    <p class="person__role">Einrichtungsleitung</p>
    <div class="person__text">
      <p>Lorem ipsum dolor sit amet, graecequidameoste, facetedic eretvituperatoribusest at. Odioeratmnesarchumeiusu, neclabi turlobortis at. Est albucius mandamus et. Ut pro option omn esque, accusatapartiendosedte. Euiusatquiignota maiorum. His nominaviexpetendainteresset an, te vitae abhorreanteum. Eiha rumfierent vel. Eos eutheophrastusdefinitionem. Quo appetere tractatossententiae id, ut duo hinctempor, omnesnominavisad ipscingeumei. Necutnonumylaborelobortis, quod interesset persequeris cu qui. Cu cum oportereconcludaturque. Intelle gamcomprehensam in pro. Cum an dicam consul vivendo, no mutatdolore qui.</p>
      <p>Lorem ipsum dolor sit amet, graecequidameoste, facetedic eretvituperatoribusest at. Odioeratmnesarchumeiusu, neclabi turlobortis at. Est albucius mandamus et. Ut pro option omn esque, accusatapartiendosedte. Euiusatquiignota maiorum. His nominaviexpetendainteresset an, te vitae abhorreanteum. Eiha rumfierent vel. Eos eutheophrastusdefinitionem. Quo appetere tractatossententiae id, ut duo hinctempor, omnesnominavisad ipscingeumei. Necutnonumylaborelobortis, quod interesset persequeris cu qui. Cu cum oportereconcludaturque. Intelle gamcomprehensam in pro. Cum an dicam consul vivendo, no mutatdolore qui.</p>
    </div>
    <p class="person__contact"><b>T:</b> 0 40 12 | 5 67 - 104<br><b>E-mail:</b> jbrettschneider@jugendverbund-kl.de</p>
    <span class="folio">01</span>
  </article>
</section>

</body>
</html>
```